Package design for quilted mattress covers.

We are producing a comfortable "quilted mattress protector" for beds . We need a very elegant and attractive and cozy insert label. approx. size is 14 inches high x11 inches wide. (One base design with slight edits to customize for each different bed size) It will be packaged in a nice clear bag, with the design label in front. I attached the type of product for reference

package text:
QUILTED MATTRESS COVER

size: 33x75x10"

*ultimate comfort
*breathable cotton top
*waterproof lining
*easy care wash and dry
Updates

Target Market(s)

displayed in drygood and bedding retail stores

Colors

Designer to choose colors to be used in the design.

Requirements
Must have
• all info as in description
Nice to have
• an image of a quilted cover on a bed, professionally included in the package design
Should not have
• ..

```html
<!DOCTYPE html>
<html lang="en">
<head>
<meta charset="utf-8">
<title>Quilted Mattress Cover – Insert Label</title>
<link href="https://fonts.googleapis.com/css2?family=Poppins:wght@700&family=Questrial&family=Oswald:wght@500&display=swap" rel="stylesheet">
<style>
  :root {
    --navy: #0e2a4f;
    --navy-line: #3a5170;
    --teal: #16807c;
    --teal-icon: #1b7d78;
    --white: #ffffff;
    --ink: #14345a;
    --page: #f4f4f2;
  }
  * { box-sizing: border-box; margin: 0; padding: 0; }
  html, body { width: 1200px; height: 847px; overflow: hidden; background: var(--page); }
  .label {
    position: absolute; left: 301px; top: 22px;
    width: 598px; height: 802px;
    background: var(--navy);
    border: 7px solid var(--navy);
  }
  .header {
    height: 202px; text-align: center; color: var(--white);
  }
  .title {
    font-family: "Poppins", sans-serif; font-weight: 700;
    font-size: 106px; line-height: 1; letter-spacing: 1px;
    padding-top: 28px;
  }
  .subtitle {
    font-family: "Oswald", sans-serif; font-weight: 500;
    font-size: 54px; line-height: 1; color: var(--teal);
    letter-spacing: 2px; margin-top: 8px;
  }
  .photo {
    position: relative; height: 534px;
    background:
      radial-gradient(ellipse at 85% 20%, rgba(168,150,190,0.45), transparent 30%),
      radial-gradient(ellipse at 15% 12%, rgba(196,176,140,0.55), transparent 28%),
      linear-gradient(180deg, #e3dfd6 0%, #ece9e3 40%, #f3f3f1 62%, #e9ebec 100%);
  }
  .features {
    position: absolute; left: 42px; top: 200px; list-style: none;
  }
  .feature {
    display: flex; align-items: center; height: 54px; margin-bottom: 20px;
  }
  .feature-icon {
    width: 54px; height: 54px; border-radius: 8px;
    background: var(--teal-icon); flex: none;
  }
  .feature-text {
    font-family: "Questrial", sans-serif; font-size: 24px;
    color: var(--ink); text-decoration: underline; margin-left: 12px;
  }
  .sizes {
    display: flex; gap: 4px; height: 52px; padding: 5px 2px 0;
    background: var(--navy);
  }
  .size {
    flex: 1; border: 1px solid var(--navy-line);
    display: flex; align-items: center; padding-left: 12px; gap: 14px;
    color: var(--white); font-family: "Poppins", sans-serif; font-size: 22px;
  }
  .size-box { width: 17px; height: 17px; background: var(--white); }
</style>
</head>
<body>
  <main class="label">
    <header class="header">
      <h1 class="title">QUILTED</h1>
      <p class="subtitle">MATTRESS COVER</p>
    </header>

    <section class="photo" role="img" aria-label="Bright bedroom with pillows on a white quilted mattress cover, lavender and lemons on a side table">
      <ul class="features">
        <li class="feature">
          <svg class="feature-icon" viewBox="0 0 54 54" aria-hidden="true">
            <rect width="54" height="54" rx="8" fill="var(--teal-icon)"/>
            <circle cx="22" cy="16" r="5" fill="none" stroke="#fff" stroke-width="3"/>
            <path d="M27 18 L33 10 M22 22 V38 Q22 44 28 44 H32 Q36 44 36 38 V26 Q36 22 32 22 H26" fill="none" stroke="#fff" stroke-width="3" stroke-linecap="round"/>
          </svg>
          <span class="feature-text">Ultimate comfort</span>
        </li>
        <li class="feature">
          <svg class="feature-icon" viewBox="0 0 54 54" aria-hidden="true">
            <rect width="54" height="54" rx="8" fill="var(--teal-icon)"/>
            <g fill="none" stroke="#fff" stroke-width="2.5">
              <circle cx="21" cy="20" r="7"/><circle cx="33" cy="20" r="7"/>
              <circle cx="27" cy="29" r="7"/>
              <path d="M27 36 V46 M20 40 L27 44 L34 40"/>
            </g>
          </svg>
          <span class="feature-text">Breathable cotton top</span>
        </li>
        <li class="feature">
          <svg class="feature-icon" viewBox="0 0 54 54" aria-hidden="true">
            <rect width="54" height="54" rx="8" fill="var(--teal-icon)"/>
            <circle cx="27" cy="27" r="17" fill="none" stroke="#fff" stroke-width="3"/>
            <path d="M27 15 Q19 26 19 31 A8 8 0 0 0 35 31 Q35 26 27 15Z" fill="#fff"/>
            <path d="M15 39 L39 15" stroke="var(--teal-icon)" stroke-width="6"/>
            <path d="M15 39 L39 15" stroke="#fff" stroke-width="3"/>
          </svg>
          <span class="feature-text">Waterproof lining</span>
        </li>
        <li class="feature">
          <svg class="feature-icon" viewBox="0 0 54 54" aria-hidden="true">
            <rect width="54" height="54" rx="8" fill="var(--teal-icon)"/>
            <rect x="12" y="10" width="30" height="34" rx="3" fill="none" stroke="#fff" stroke-width="3"/>
            <path d="M12 18 H42" stroke="#fff" stroke-width="2.5"/>
            <circle cx="27" cy="31" r="8" fill="none" stroke="#fff" stroke-width="3"/>
            <circle cx="36" cy="14" r="1.6" fill="#fff"/>
          </svg>
          <span class="feature-text">Easy care wash and dry</span>
        </li>
      </ul>
    </section>

    <footer class="sizes" aria-label="Bed sizes">
      <div class="size"><span class="size-box"></span></div>
      <div class="size"><span class="size-box"></span></div>
      <div class="size"><span class="size-box"></span></div>
      <div class="size">
        <svg width="17" height="17" viewBox="0 0 17 17" aria-hidden="true">
          <rect width="17" height="17" fill="#fff"/>
          <path d="M4 4 L13 13 M13 4 L4 13" stroke="var(--navy)" stroke-width="2.4"/>
        </svg>
        <span>K</span>
      </div>
      <div class="size"><span class="size-box"></span></div>
      <div class="size"><span class="size-box"></span></div>
    </footer>
  </main>
</body>
</html>
```